ultra-minimalist business card

front (black background, matte):

tarik b. hosseny
writer | photographer
get@tarikhosseny.com

back (white background, matte):

a picture speaks a thousand words;
a word draws a thousand pictures.

www.tarikhosseny.com

all text should be small (white or silver - as long as it shows against the black - on the front; black or gray - as long as it shows against the white - on the back).

feel free to get creative in terms of arrangement, alignment, and font type, but remember, the overall style is minimalist, so nothing too fancy, please.

thanks.

```html
<!DOCTYPE html>
<html lang="en">
<head>
<meta charset="utf-8">
<title>tarik b. hosseny — card back</title>
<link rel="stylesheet" href="https://fonts.googleapis.com/css2?family=Work+Sans:wght@300;400&family=Arimo:wght@400&display=swap">
<style>
  :root {
    --page: #ffffff;
    --card: #f1f1ef;
    --rule: #e6e6e4;
    --ink-soft: #6e6e6e;
    --ink-strong: #2a2a2a;
    --ink-url: #8a8a8a;
  }
  html, body {
    margin: 0;
    padding: 0;
    width: 1200px;
    height: 805px;
    overflow: hidden;
    background: var(--page);
  }
  .canvas {
    position: relative;
    width: 1200px;
    height: 805px;
  }
  .card {
    position: absolute;
    left: 40px;
    top: 40px;
    width: 1116px;
    height: 727px;
    background: var(--card);
    overflow: hidden;
  }
  .card__rules {
    position: absolute;
    inset: 0;
  }
  .quote {
    position: absolute;
    left: 0;
    right: 0;
    top: 314px;
    margin: 0;
    text-align: center;
    font-family: "Work Sans", sans-serif;
    font-weight: 300;
    font-size: 37px;
    line-height: 45px;
    letter-spacing: 1.6px;
    color: var(--ink-soft);
  }
  .quote__key {
    font-weight: 400;
    color: var(--ink-strong);
  }
  .card__url {
    position: absolute;
    left: 0;
    right: 0;
    top: 622px;
    margin: 0;
    text-align: center;
    font-family: "Arimo", sans-serif;
    font-size: 22px;
    color: var(--ink-url);
  }
</style>
</head>
<body>
  <div class="canvas">
    <section class="card">
      <svg class="card__rules" width="1116" height="727" viewBox="0 0 1116 727" aria-hidden="true">
        <line x1="0" y1="371" x2="1116" y2="646" stroke="var(--rule)" stroke-width="3"/>
        <line x1="0" y1="499" x2="273" y2="727" stroke="var(--rule)" stroke-width="3"/>
      </svg>
      <p class="quote">
        a <span class="quote__key">picture</span> speaks a thousand words;<br>
        a <span class="quote__key">word</span> draws a thousand pictures
      </p>
      <p class="card__url">tarikhosseny.com</p>
    </section>
  </div>
</body>
</html>
```